Label for Dog Nourishing CBD Balm

Dear Designers,

We are looking for a packaging expert to design our new Hydrating Balm for dogs which contain a relaxing hemp extract (CBD). The product is intended to be massaged on the dog’s paws to make them softer and promote the animal’s well-being :)

Our company is already selling various relaxing cat & dog products, and we would like this new design to reflect the same "style & feeling" as our current products (see attached ZIP file).

Technical aspects:
- The packaging is a 40ml aluminium jar (58mm x 23mm).
- We are looking to design 2 separate labels (one for the front, one for the back)
- The label dimensions should be : 50mm x 50mm
- Please follow technical guidelines from printer (see ZIP file).

Design aspects:
- The design should be compatible with our brand identity (i.e. fluffly, pure, relaxing, positive, clean & natural).
- People should understand what the product "is" and what the product "does" simply from looking at the design.
- The actual balm is white/yellow in color.
- Soft/rounded shapes are preferred.
- Please use our brand's colors (see typo & colors in ZIP file)
- Please use our brand's fonts (see typo & colors in ZIP file)
- Please use our company logo (see ZIP file).
- The design also needs to convey a strong sense of professionalism as we are an animal "healthcare" brand.
- If you want to include a dog picture, we would prefer you to use a picture of our official brand ambassador (see ZIP file).
- Only original work (no plagiarism will be accepted).

Please don't hesitate to send us a message if you have any questions about the brand, the product or the design requirements.

We look forward to seeing your designs & working on this together !

Thanks & regards,
Marcus

Target Market(s)

Dog owners

Font styles to use
Other font styles liked:
• See ZIP file

Requirements
Must have
• Brand fonts (see typo & colors in ZIP file)
Brand colors (see typo & colors in ZIP file)

```html
<!DOCTYPE html>
<html lang="en">
<head>
<meta charset="utf-8">
<title>VerdaBalm Soothing Balm – Jar Labels</title>
<link rel="stylesheet" href="https://fonts.googleapis.com/css2?family=Quicksand:wght@500;600;700&display=swap">
<style>
  :root {
    --green: #2f9d78;
    --green-soft: #8cc6ae;
    --green-dark: #173a29;
    --orange: #f5b574;
    --grey-band: #dedfe0;
    --grey-line: #d6d6d6;
    --ink: #2b2b2b;
    --paper: #ffffff;
    --backdrop: #f1f1f1;
  }
  * { box-sizing: border-box; margin: 0; padding: 0; }
  html, body { width: 1200px; height: 941px; overflow: hidden; }
  body {
    background: var(--backdrop);
    font-family: "Quicksand", sans-serif;
    color: var(--ink);
    position: relative;
  }
  .label {
    position: absolute;
    top: 220px;
    width: 500px;
    height: 500px;
    border-radius: 50%;
    background: var(--paper);
    overflow: hidden;
    box-shadow: 0 4px 18px rgba(0,0,0,0.08);
  }
  .label--front { left: 70px; }
  .label--back { left: 630px; }

  /* Front label */
  .front-art { position: absolute; inset: 0; z-index: 2; pointer-events: none; }
  .front-deco { position: absolute; inset: 0; z-index: 0; }
  .brand {
    position: absolute;
    top: 62px; left: 0; right: 0;
    display: flex; justify-content: center; align-items: center; gap: 8px;
    font-weight: 700; font-size: 27px; letter-spacing: 0.5px;
    color: var(--green-dark);
    z-index: 1;
  }
  .brand__dot {
    width: 14px; height: 14px; border-radius: 50%;
    background: var(--green-dark);
  }
  .product-line {
    position: absolute; top: 140px; left: 0; right: 0;
    text-align: center; font-weight: 700; font-size: 38px;
    color: var(--orange); z-index: 1;
  }
  .product-name {
    position: absolute; top: 192px; left: 0; right: 0;
    text-align: center; font-weight: 700; font-size: 49px;
    color: var(--green); letter-spacing: 0.5px; z-index: 1;
  }
  .stat {
    position: absolute; top: 268px; width: 120px;
    text-align: center; line-height: 1; z-index: 1;
  }
  .stat--cbd { left: 44px; }
  .stat--thc { left: 336px; }
  .stat__value { font-weight: 700; font-size: 33px; color: var(--green-dark); }
  .stat__unit { font-weight: 600; font-size: 20px; color: var(--orange); margin-top: 6px; }
  .ambassador-photo {
    position: absolute; left: 186px; top: 284px;
    width: 128px; height: 156px;
    border-radius: 42% 42% 30% 30%;
    background: radial-gradient(ellipse at 50% 45%, #b9b3b3 0%, #d7d2d0 50%, #f4f2f1 85%);
    z-index: 1;
  }

  /* Back label */
  .copy {
    position: absolute; top: 38px; left: 0; right: 0;
    text-align: center; font-weight: 500;
    font-size: 16.5px; line-height: 22px; color: var(--ink);
  }
  .copy__heading {
    font-weight: 700; font-size: 15px; color: var(--green);
    letter-spacing: 0.3px;
  }
  .copy__block { margin-bottom: 14px; }
  .distributor {
    position: absolute; left: 0; right: 0; top: 362px; bottom: 0;
    background: var(--grey-band);
    text-align: center; font-weight: 500;
    font-size: 16px; line-height: 22px; padding-top: 10px;
  }
  .distributor__name { font-weight: 700; font-size: 18px; color: var(--green-dark); }
</style>
</head>
<body>

<section class="label label--front" aria-label="Front label">
  <svg class="front-deco" viewBox="0 0 500 500" width="500" height="500" aria-hidden="true">
    <path d="M 24 250 A 226 226 0 0 1 476 250" fill="none" stroke="var(--grey-line)" stroke-width="3"/>
    <path class="swoosh" d="M 40 190 Q 90 112 190 106 Q 230 104 250 118 Q 270 104 310 106 Q 410 112 460 190 L 452 192 Q 405 126 310 122 Q 272 120 250 134 Q 228 120 190 122 Q 95 126 48 192 Z" fill="var(--green-soft)"/>
    <path d="M 48 192 Q 95 126 190 122 Q 228 120 250 134 Q 272 120 310 122 Q 405 126 452 192" fill="none" stroke="var(--grey-line)" stroke-width="3"/>
  </svg>
  <svg class="front-art" viewBox="0 0 500 500" width="500" height="500">
    <defs>
      <path id="claim-arc" d="M 28 250 A 222 222 0 0 0 472 250"/>
    </defs>
    <text font-family="Quicksand, sans-serif" font-weight="700" font-size="25" fill="var(--green-dark)" letter-spacing="0.5">
      <textPath href="#claim-arc" startOffset="50%" text-anchor="middle">REPAIR | NOURISH | PROTECT</textPath>
    </text>
  </svg>
  <div class="brand"><span class="brand__dot"></span>VERDALIA</div>
  <div class="product-line">VerdaBalm</div>
  <div class="product-name">SOOTHING BALM</div>
  <div class="stat stat--cbd"><div class="stat__value">CBD</div><div class="stat__unit">250mg</div></div>
  <div class="stat stat--thc"><div class="stat__value">0%</div><div class="stat__unit">THC</div></div>
  <div class="ambassador-photo" role="img" aria-label="Photo of the brand ambassador, a white wrinkled shar-pei dog"></div>
</section>

<section class="label label--back" aria-label="Back label">
  <div class="copy">
    <div class="copy__block">
      <div class="copy__heading">EVERYDAY RELAXATION</div>
      This balm repairs, nourishes<br>
      and protects your dog’s sensitive skin.<br>
      Its trusted multi-action formula brings relief<br>
      to fragile areas and soothes temporary<br>
      irrations (paw pads, elbows, etc.)
    </div>
    <div class="copy__block">
      <div class="copy__heading">RECOMMENDED USE:</div>
      Rub a small amount of balm in the palm of your hand<br>
      and apply to sensitive areas as a daily care ritual. Repeat<br>
      until the product has been completely absorbed.
    </div>
    <div class="copy__block">
      <div class="copy__heading">INGREDIENTS:</div>
      Shea Butter, Beeswax, Coconut Oil,<br>
      Hemp Extract (0% THC).
    </div>
  </div>
  <div class="distributor">
    Distributed by:<br>
    <span class="distributor__name">VERDA EUROPE KFT.</span><br>
    Liget utca 14<br>
    1071 Budapest<br>
    Hungary
  </div>
</section>

</body>
</html>
```